Tandril Energy b-card redesign

I would like to redesign the card (and power point template) for tandril energy. We are a developer/owner/operator of high-tech biomass gasification power plants. We take ag waste like nut shells or fruit pits and convert that into electricity in the 1/2 - 3 MW range. I would like to change our company color from red to golden gate bridge orange (C=0,M=69,,Y=100,B=6).

Tech

```html
<!DOCTYPE html>
<html lang="en">
<head>
<meta charset="utf-8">
<title>Tandril Energy – Business Card</title>
<link rel="stylesheet" href="https://fonts.googleapis.com/css2?family=Mulish:wght@400;700&family=Cinzel:wght@500&display=swap">
<style>
  :root {
    --gg-orange: #ef6f00;
    --gg-orange-light: #f38a3a;
    --gg-orange-deep: #d85f06;
    --orange-shadow: #6b2e08;
    --card-black: #0d0d0d;
    --stage: #4a4a48;
    --stage-dark: #2b2b2a;
    --ink-light: #e9e9e9;
    --ink-muted: #a9a9a9;
  }
  * { box-sizing: border-box; margin: 0; padding: 0; }
  html, body { width: 1200px; height: 871px; overflow: hidden; }
  body {
    position: relative;
    background: radial-gradient(ellipse at 50% 40%, var(--stage) 0%, var(--stage-dark) 100%);
    font-family: "Mulish", "Century Gothic", sans-serif;
  }
  .card {
    position: absolute;
    width: 540px;
    height: 309px;
    overflow: hidden;
    box-shadow: 0 14px 30px rgba(0,0,0,.45);
  }
  /* front */
  .card--front {
    left: 80px; top: 100px;
    background: linear-gradient(135deg, var(--gg-orange-light) 0%, var(--gg-orange) 55%, var(--gg-orange-deep) 100%);
  }
  .card--front .wordmark {
    position: absolute;
    left: 0; right: 0; top: 128px;
    text-align: center;
    font-size: 30px;
    letter-spacing: 2px;
    text-transform: uppercase;
    color: #fff3ea;
  }
  .card--front .mark-dot {
    display: inline-block;
    width: 10px; height: 10px;
    margin-left: 8px;
    border-radius: 50%;
    background: #fff3ea;
    vertical-align: middle;
  }
  /* back */
  .card--back {
    left: 580px; top: 452px;
    background: var(--card-black);
    color: var(--ink-muted);
  }
  .card--back .wordmark {
    position: absolute;
    left: 60px; top: 30px;
    font-size: 24px;
    letter-spacing: 1.5px;
    text-transform: uppercase;
    color: var(--ink-light);
  }
  .card--back .wordmark .mark-dot {
    display: inline-block;
    width: 8px; height: 8px;
    margin-left: 6px;
    border-radius: 50%;
    background: var(--gg-orange);
    vertical-align: middle;
  }
  .address {
    position: absolute;
    left: 60px; top: 90px;
    font-size: 11px;
    line-height: 16px;
  }
  .contacts {
    position: absolute;
    left: 42px; top: 142px;
    list-style: none;
    font-size: 11.5px;
    line-height: 18px;
  }
  .contacts li { display: flex; align-items: center; }
  .contacts svg { width: 10px; height: 10px; margin-right: 9px; }
  .person {
    position: absolute;
    right: 38px; top: 178px;
    text-align: right;
  }
  .person__name {
    font-weight: 700;
    font-size: 15px;
    color: var(--gg-orange);
  }
  .person__role {
    font-size: 11px;
    margin-top: 6px;
    color: var(--ink-muted);
  }
  .corner-disc {
    position: absolute;
    left: 200px; top: 190px;
    width: 190px; height: 190px;
    border-radius: 50%;
    background: var(--gg-orange);
    box-shadow: 0 0 0 10px var(--orange-shadow);
  }
  .caption {
    position: absolute;
    left: 34px; top: 786px;
    font-family: "Cinzel", serif;
    font-weight: 500;
    font-size: 30px;
    letter-spacing: 2px;
    color: #ffffff;
  }
</style>
</head>
<body>
  <section class="card card--front" aria-label="Card front">
    <p class="wordmark">Tandril Energy<span class="mark-dot"></span></p>
  </section>

  <section class="card card--back" aria-label="Card back">
    <p class="wordmark">Tandril Energy<span class="mark-dot"></span></p>
    <p class="address">PO Box 48213<br>Oakland, CA 94607</p>
    <ul class="contacts">
      <li><svg viewBox="0 0 10 10"><circle cx="5" cy="5" r="5" fill="#ef6f00"/><path d="M3 3.2h1.3l.4 1.2-.7.5a3 3 0 0 0 1.3 1.3l.5-.7 1.2.4V7.2A4.4 4.4 0 0 1 3 3.2z" fill="#0d0d0d"/></svg>510.555.0142</li>
      <li><svg viewBox="0 0 10 10"><rect width="10" height="10" rx="2" fill="#ef6f00"/><rect x="2.5" y="3" width="5" height="4" fill="#0d0d0d"/></svg>510.555.0187</li>
      <li><svg viewBox="0 0 10 10"><rect width="10" height="10" rx="2" fill="#ef6f00"/><path d="M2 3h6v4H2z M2 3l3 2.2L8 3" fill="none" stroke="#0d0d0d" stroke-width=".8"/></svg>reyes@tandrilenergy.net</li>
      <li><svg viewBox="0 0 10 10"><circle cx="5" cy="5" r="5" fill="#ef6f00"/><circle cx="5" cy="5" r="2.6" fill="none" stroke="#0d0d0d" stroke-width=".8"/></svg>www.tandrilenergy.net</li>
    </ul>
    <div class="corner-disc"></div>
    <div class="person">
      <p class="person__name">Marcus Allen Reyes</p>
      <p class="person__role">CFO</p>
    </div>
  </section>

  <p class="caption">PERSONAL BUSINESSCARD</p>
</body>
</html>
```